Jackpot Display Wallpaper Design

We develop Jackpot Systems for Casinos and have a web based Jackpot Odometer display. Our software works by superimposing dynamic content over a fixed background.

We require the design of a fixed background of dimensions 1920 x 1080 incorporating higher quality graphical design work and creative ideas.

See File 4 below - "High Hand TEMPLATE". The finished work will resemble this image, with the grey background replaced with your creative design. The black panels will be replaced with your panels, with nice borders and interior shading or pattern. Our software will dynamically superimpose content over the panels. The panels should be of similar size and location to those shown although this is not strictly rigid and you can relocate or resize panels to a limited extent.

The end result when our software runs is something like File 5 below - "High Hand SAMPLE RESULT". Note that the example shows a patterned blue background, a red logo area, and grey shading within the panels.

The text within the panels is rendered dynamically by our application.

** This is a very plain design and only intended to illustrate how we superimpose text and playing cards onto a background. Do not take any design cues from this image.

Please provide the background, and blank panels. The panels can (and should) have some texture or shading that will look good when we render text over them.

Feel free to suggest a font and/or text color that you think would look good against your background and we can render the content in the font / color you suggest.

Target Market(s)

Poker Room facilities and Casinos

Industry/Entity Type

Software

Font styles to use
Sans Serif

Requirements
Must have
• - A graphic design based on the template called High Hand TEMPLATE.
• - 1920 x 1080 Photoshop image using separate layers.
• - The design needs to be edgy and reflect gaming, casinos and poker rooms.
Nice to have
• -Please see files 1, 2, and 3 below by way of "edgy" style guide.
• - For files 1, 2, 3 - ignore the "Bad Beat" wording but focus on the design style by way of example.
• - The background may or may not include the words "Poker" and / or "Jackpot"
• - You can fill in the panels with some sample content to illustrate how it will look.
• - The area at bottom containing scrolling text may be a frame with a border or just an area where we superimpose the scrolling text.

```html
<!DOCTYPE html>
<html lang="en">
<head>
<meta charset="utf-8">
<title>Royal Flush Jackpot Display</title>
<link rel="stylesheet" href="https://fonts.googleapis.com/css2?family=Archivo+Black&family=Arimo:wght@700&display=swap">
<style>
  :root {
    --bg-light: #f2f2f4;
    --bg-mid: #d9d9dd;
    --bg-dark: #bcbcc2;
    --panel-black: #0d0d0d;
    --panel-edge: #3a3a3a;
    --panel-shine: #4a4a4a;
    --rod: #9a9a9a;
    --rod-light: #e6e6e6;
    --text-white: #ffffff;
    --card-white: #fdfdfd;
    --suit-red: #e0121b;
    --suit-black: #111111;
    --logo-grey: #d6d6d6;
  }
  * { box-sizing: border-box; margin: 0; padding: 0; }
  html, body { width: 1200px; height: 675px; overflow: hidden; }
  body {
    position: relative;
    font-family: "Arimo", Arial, sans-serif;
    color: var(--text-white);
    background:
      repeating-linear-gradient(90deg,
        rgba(255,255,255,0.0) 0px, rgba(255,255,255,0.55) 14px,
        rgba(0,0,0,0.06) 30px, rgba(255,255,255,0.0) 46px),
      radial-gradient(ellipse at 50% 45%, var(--bg-light) 0%, var(--bg-mid) 65%, var(--bg-dark) 100%);
  }
  .rod {
    position: absolute; width: 5px;
    background: linear-gradient(90deg, var(--rod), var(--rod-light), var(--rod));
  }
  .bar {
    position: absolute; left: 378px; width: 444px;
    display: flex; align-items: center; justify-content: center;
    background: linear-gradient(180deg, var(--panel-shine) 0%, var(--panel-black) 35%, var(--panel-black) 70%, #222 100%);
    border-radius: 4px;
    box-shadow: 0 3px 6px rgba(0,0,0,0.45);
    font-size: 18px; letter-spacing: 0.5px; text-transform: uppercase;
  }
  .bar--title { top: 165px; height: 38px; }
  .bar--bonus { top: 390px; height: 40px; }
  .bar--winner { top: 587px; height: 40px; text-transform: none; font-size: 18px; }

  .logo-sign {
    position: absolute; left: 448px; top: 22px; width: 300px; height: 96px;
  }
  .logo-sign svg { position: absolute; inset: 0; }
  .logo-name {
    position: absolute; inset: 0; display: flex; align-items: center; justify-content: center;
    font-size: 34px; color: var(--logo-grey); letter-spacing: 1px;
  }

  .tube {
    position: absolute; left: 0; top: 240px; width: 1200px; height: 72px;
    background: linear-gradient(180deg, #2c2c2c 0%, #050505 40%, #111 75%, #3a3a3a 100%);
    box-shadow: 0 4px 8px rgba(0,0,0,0.35);
  }
  .odometer {
    position: absolute; left: 133px; top: 213px; width: 940px; height: 140px;
    display: flex;
  }
  .drum {
    position: relative; flex: 1; margin: 0 1px;
    border-radius: 14px;
    background: linear-gradient(180deg, #3c3c3c 0%, #0a0a0a 18%, #141414 50%, #0a0a0a 82%, #3c3c3c 100%);
    box-shadow: inset 0 0 0 2px var(--panel-edge), 0 4px 10px rgba(0,0,0,0.5);
    font-family: "Archivo Black", "Arial Black", sans-serif;
    font-size: 140px; line-height: 140px; text-align: center;
  }
  .drum--comma::after {
    content: ","; position: absolute; right: -16px; bottom: 4px;
    font-size: 80px; line-height: 80px; z-index: 2;
  }

  .wing {
    position: absolute; top: 443px; width: 150px; height: 120px;
  }
  .wing svg { position: absolute; inset: 0; }
  .wing--prize { left: 272px; }
  .wing--countdown { left: 778px; }
  .wing-label {
    position: absolute; left: 0; right: 0; text-align: center; font-size: 15px;
  }
  .wing-value {
    position: absolute; left: 0; right: 0; text-align: center; font-size: 28px;
  }
  .wing--prize .wing-label { top: 32px; left: 10px; right: 30px; }
  .wing--prize .wing-value { top: 52px; left: 10px; right: 30px; }
  .wing--countdown .wing-label { top: 34px; left: 28px; right: 4px; font-size: 12px; }
  .wing--countdown .wing-value { top: 52px; left: 28px; right: 4px; }

  .card-tray {
    position: absolute; left: 392px; top: 436px; width: 416px; height: 140px;
    border-radius: 10px;
    background: linear-gradient(180deg, #3a3a3a 0%, #080808 20%, #151515 60%, #0a0a0a 85%, #333 100%);
    box-shadow: 0 4px 10px rgba(0,0,0,0.5);
    display: flex; justify-content: center; align-items: center; gap: 14px;
  }
  .card {
    position: relative; width: 68px; height: 98px; border-radius: 4px;
    background: linear-gradient(160deg, var(--card-white), #e6e6e6);
    font-family: Arial, sans-serif; font-weight: 700;
  }
  .card--red { color: var(--suit-red); }
  .card--black { color: var(--suit-black); }
  .card-corner { position: absolute; font-size: 9px; line-height: 9px; text-align: center; }
  .card-corner--top { left: 3px; top: 4px; }
  .card-corner--bottom { right: 3px; bottom: 4px; transform: rotate(180deg); }
  .card-suit {
    position: absolute; inset: 0; display: flex; align-items: center; justify-content: center; font-size: 22px;
  }

  .news-band {
    position: absolute; left: 0; top: 633px; width: 1200px; height: 42px;
    background: linear-gradient(180deg, #3a3a3a 0%, #060606 30%, #111 100%);
    display: flex; align-items: center; justify-content: center;
    font-size: 18px; text-transform: uppercase;
  }
</style>
</head>
<body>
  <div class="rod" style="left:597px;top:0;height:26px"></div>
  <div class="rod" style="left:506px;top:112px;height:56px"></div>
  <div class="rod" style="left:689px;top:112px;height:56px"></div>

  <div class="logo-sign">
    <svg width="300" height="96" viewBox="0 0 300 96">
      <defs>
        <linearGradient id="signFill" x1="0" y1="0" x2="0" y2="1">
          <stop offset="0" stop-color="#4a4a4a"/>
          <stop offset="0.3" stop-color="#0c0c0c"/>
          <stop offset="1" stop-color="#1c1c1c"/>
        </linearGradient>
      </defs>
      <path d="M4 4 Q150 14 296 4 L276 90 Q150 82 24 90 Z" fill="url(#signFill)" stroke="#2c2c2c" stroke-width="2"/>
    </svg>
    <div class="logo-name">YOUR LOGO</div>
  </div>

  <div class="bar bar--title">Royal Flush Jackpot</div>

  <div class="tube"></div>
  <div class="odometer" aria-label="Jackpot amount 256,111.95">
    <div class="drum">2</div>
    <div class="drum">5</div>
    <div class="drum drum--comma">6</div>
    <div class="drum">1</div>
    <div class="drum">1</div>
    <div class="drum drum--comma">1</div>
    <div class="drum">9</div>
    <div class="drum">5</div>
  </div>

  <div class="rod" style="left:474px;top:428px;height:12px"></div>
  <div class="rod" style="left:719px;top:428px;height:12px"></div>
  <div class="bar bar--bonus">High Hand Bonus</div>

  <div class="wing wing--prize">
    <svg width="150" height="120" viewBox="0 0 150 120">
      <defs>
        <linearGradient id="wingFill" x1="0" y1="0" x2="0" y2="1">
          <stop offset="0" stop-color="#444"/>
          <stop offset="0.25" stop-color="#0b0b0b"/>
          <stop offset="1" stop-color="#1a1a1a"/>
        </linearGradient>
      </defs>
      <path d="M2 2 L150 10 L150 112 L20 118 Q10 60 2 2 Z" fill="url(#wingFill)"/>
    </svg>
    <div class="wing-label">PRIZE</div>
    <div class="wing-value">$250</div>
  </div>

  <div class="wing wing--countdown">
    <svg width="150" height="120" viewBox="0 0 150 120">
      <path d="M0 10 L148 2 Q140 60 130 118 L0 112 Z" fill="url(#wingFill)"/>
    </svg>
    <div class="wing-label">COUNTDOWN</div>
    <div class="wing-value">1:59</div>
  </div>

  <div class="card-tray">
    <div class="card card--red">
      <span class="card-corner card-corner--top">A<br>♥</span>
      <span class="card-suit">♥</span>
      <span class="card-corner card-corner--bottom">A<br>♥</span>
    </div>
    <div class="card card--black">
      <span class="card-corner card-corner--top">A<br>♣</span>
      <span class="card-suit">♣</span>
      <span class="card-corner card-corner--bottom">A<br>♣</span>
    </div>
    <div class="card card--red">
      <span class="card-corner card-corner--top">A<br>♦</span>
      <span class="card-suit">♦</span>
      <span class="card-corner card-corner--bottom">A<br>♦</span>
    </div>
    <div class="card card--black">
      <span class="card-corner card-corner--top">A<br>♠</span>
      <span class="card-suit">♠</span>
      <span class="card-corner card-corner--bottom">A<br>♠</span>
    </div>
  </div>

  <div class="rod" style="left:474px;top:574px;height:16px"></div>
  <div class="rod" style="left:719px;top:574px;height:16px"></div>
  <div class="bar bar--winner">Two Pair - Table 18 (Sam Carter)</div>

  <div class="rod" style="left:474px;top:626px;height:10px"></div>
  <div class="rod" style="left:719px;top:626px;height:10px"></div>
  <div class="news-band">Text News Here</div>
</body>
</html>
```